Lark Ridge Property Biz Card
Business card and stationary
Project: Lark Ridge Property Biz Card
Lark Ridge Property Biz Card - Real Estate
Creative Brief
Professional
Dwight Fenmore
DO NOT ADD AN ADDRESS
dfenmore@larkridgeproperty.com
On the front I would like the logo, my name, phone number and email address. Also please have the catch phrase: "We buy houses, any condition! Get Cash Fast! Quick Closing!" The colour scheme of my logo is not set in stone, so please feel free to experiment with the colours.
On the back of the card please have the company logo

```html
<!DOCTYPE html>
<html lang="en">
<head>
<meta charset="utf-8">
<title>Lark Ridge Property – Business Card</title>
<link href="https://fonts.googleapis.com/css2?family=Arimo:wght@400;700&display=swap" rel="stylesheet">
<style>
  :root {
    --brand-blue: #22497f;
    --brand-blue-soft: #2d5690;
    --ink: #2a2a2a;
    --card-white: #ffffff;
    --stage: #e6e7e9;
    --illustration-light: #eef0f3;
    --illustration-mid: #e2e5ea;
    --bar-dark: #1c1c1c;
  }
  * { box-sizing: border-box; margin: 0; padding: 0; }
  html, body {
    width: 1200px; height: 768px; overflow: hidden;
    background: var(--stage);
    font-family: "Arimo", Arial, sans-serif;
  }
  .stage { position: relative; width: 1200px; height: 768px; }
  .card {
    position: absolute; width: 451px; height: 276px; overflow: hidden;
    background: var(--card-white);
    box-shadow: 0 4px 14px rgba(0,0,0,.25);
  }
  .card--front { left: 120px; top: 96px; }
  .card--back-light { left: 629px; top: 96px; }
  .card--back-blue { left: 374px; top: 440px; background: var(--brand-blue); }

  /* front */
  .front-band {
    position: absolute; left: 31px; top: 0; width: 30px; height: 100%;
    background: var(--brand-blue);
  }
  .front-bars { position: absolute; left: 0; top: 24px; width: 61px; }
  .front-bars span {
    display: block; height: 7px; margin-bottom: 6px; background: var(--bar-dark);
  }

  /* logo lockup: plain square + company name */
  .logo { position: absolute; display: flex; align-items: center; gap: 8px; }
  .logo-mark { flex: none; background: currentColor; }
  .logo-name {
    font-weight: 700; text-transform: uppercase; line-height: 1.05; letter-spacing: .5px;
  }
  .card--front .logo { left: 296px; top: 40px; color: var(--brand-blue); }
  .card--front .logo-mark { width: 22px; height: 22px; }
  .card--front .logo-name { font-size: 17px; }

  .front-info { position: absolute; left: 92px; top: 146px; }
  .front-name { color: var(--brand-blue); font-size: 19px; margin-bottom: 12px; }
  .front-tagline { color: var(--brand-blue); font-size: 12.5px; line-height: 1.3; margin-bottom: 14px; }
  .front-contact { color: var(--ink); font-size: 10.5px; line-height: 1.45; }

  /* backs */
  .back-illustration { position: absolute; left: 0; top: 0; width: 62%; height: 100%; }
  .card--back-light .back-illustration {
    background: linear-gradient(160deg, var(--illustration-light), var(--illustration-mid));
  }
  .card--back-blue .back-illustration {
    background: linear-gradient(160deg, var(--brand-blue-soft), var(--brand-blue));
  }
  .card--back-light .logo { left: 232px; top: 112px; color: var(--brand-blue); }
  .card--back-light .logo-mark { width: 34px; height: 34px; }
  .card--back-light .logo-name { font-size: 30px; }
  .card--back-blue .logo { left: 300px; top: 118px; color: var(--card-white); }
  .card--back-blue .logo-mark { width: 20px; height: 20px; }
  .card--back-blue .logo-name { font-size: 17px; }
</style>
</head>
<body>
<main class="stage">

  <section class="card card--front" aria-label="Business card front">
    <div class="front-band"></div>
    <div class="front-bars"><span></span><span></span><span></span></div>
    <div class="logo"><span class="logo-mark"></span><span class="logo-name">Lark Ridge<br>Property</span></div>
    <div class="front-info">
      <p class="front-name">Dwight Fenmore</p>
      <p class="front-tagline">"We buy houses, any condition!<br>Get Cash Fast! Quick Closing!"</p>
      <p class="front-contact">P: 555-014-2273<br>E: dfenmore@larkridgeproperty.com</p>
    </div>
  </section>

  <section class="card card--back-light" aria-label="Business card back, light">
    <div class="back-illustration" role="img" aria-label="Faint line illustration of a cable bridge and house rooftops"></div>
    <div class="logo"><span class="logo-mark"></span><span class="logo-name">Lark Ridge<br>Property</span></div>
  </section>

  <section class="card card--back-blue" aria-label="Business card back, blue">
    <div class="back-illustration" role="img" aria-label="Faint line illustration of a cable bridge and house rooftops"></div>
    <div class="logo"><span class="logo-mark"></span><span class="logo-name">Lark Ridge<br>Property</span></div>
  </section>

</main>
</body>
</html>
```